Yard Signs - Fiber Optic Customer

I need an awesome design for a yard sign for our new customers.  We are installing a fiber optic network and are going to give new customers the option to put a yard sign up in exchange for a free month of service.  I want to use plankmerle.example.  A blank template is available there for the large (27x18) yard signs.
Requirements:
-our website is (needs to be on sign):  www.dovernetlink.example
-our phone:  555-814-2063
-our logo
-a graphic that conveys 'connected'
I want it to say something to the effect.. I'm connected to Dovern Fiber.  The fastest high-speed internet available.  Crystal clear telephone.  I don't necessarily need that specific wording, something along those lines.
Contact me with questions:  paul@dovernetlink.example

```html
<!DOCTYPE html>
<html lang="en">
<head>
<meta charset="utf-8">
<title>Dovern Fiber Yard Sign</title>
<link rel="stylesheet" href="https://fonts.googleapis.com/css2?family=Exo+2:ital,wght@0,500;0,600;0,700;0,800;1,700;1,800&display=swap">
<style>
  :root {
    --frame: #5fe1e9;
    --corner-dark: #174f86;
    --corner-light: #3aa5cc;
    --brand-blue: #2e8cc6;
    --headline: #2a86c0;
    --contact-grey: #8a9898;
    --ink: #111111;
    --wire: #3a4fe8;
    --node-ring: #48c6d8;
    --bg-center: #ffffff;
    --bg-edge: #c9cdd0;
  }
  * { margin: 0; padding: 0; box-sizing: border-box; }
  html, body { width: 1200px; height: 807px; overflow: hidden; background: #ffffff; }
  .sign {
    position: relative;
    width: 1200px;
    height: 807px;
    border: 12px solid var(--frame);
    background: radial-gradient(ellipse at 50% 45%, var(--bg-center) 30%, #eceef0 65%, var(--bg-edge) 100%);
    font-family: "Exo 2", sans-serif;
    overflow: hidden;
  }
  .circuit-backdrop {
    position: absolute;
    inset: 0;
    background: linear-gradient(180deg, rgba(227,235,245,0.0) 0%, rgba(227,235,245,0.55) 45%, rgba(227,235,245,0.35) 100%);
  }
  .wires { position: absolute; left: -12px; top: -12px; width: 1200px; height: 807px; }
  .corner-banner { position: absolute; left: -12px; top: -12px; width: 260px; height: 300px; }
  .corner-text {
    position: absolute;
    left: -44px;
    top: 40px;
    width: 250px;
    transform: rotate(-52deg);
    color: #ffffff;
    font-weight: 700;
    font-size: 26px;
    line-height: 27px;
    text-align: center;
    letter-spacing: 1px;
  }
  .brand {
    position: absolute;
    left: 268px;
    top: 14px;
    display: flex;
    align-items: center;
    gap: 22px;
  }
  .brand-dot { width: 56px; height: 56px; border-radius: 50%; background: var(--brand-blue); }
  .brand-name {
    color: var(--brand-blue);
    font-weight: 800;
    font-size: 138px;
    line-height: 150px;
    letter-spacing: 8px;
  }
  .contact {
    position: absolute;
    left: 356px;
    top: 170px;
    color: var(--contact-grey);
    font-weight: 600;
    font-size: 42px;
    letter-spacing: -0.5px;
    word-spacing: 2px;
  }
  .contact .phone { margin-left: 40px; letter-spacing: 3px; }
  .headline {
    position: absolute;
    left: 0;
    right: 0;
    top: 318px;
    text-align: center;
    color: var(--headline);
    font-weight: 700;
    font-size: 70px;
    line-height: 84px;
    padding-right: 22px;
  }
  .headline .fiber { font-size: 66px; letter-spacing: 3px; }
  .headline .fast { display: inline-block; font-style: italic; font-weight: 800; font-size: 104px; line-height: 96px; letter-spacing: 6px; }
  .more {
    position: absolute;
    left: 70px;
    top: 720px;
    color: var(--ink);
    font-weight: 700;
    font-size: 40px;
    white-space: nowrap;
  }
  .more .url { font-weight: 800; letter-spacing: 2px; margin-left: 12px; }
</style>
</head>
<body>
<div class="sign">
  <div class="circuit-backdrop" role="img" aria-label="Faint light-blue circuit board lines across the background"></div>

  <svg class="wires" viewBox="0 0 1200 807" aria-hidden="true">
    <polyline points="196,196 196,425 385,425 385,612 805,612 805,362 1047,362 1047,218 1135,218 1135,92"
      fill="none" stroke="var(--wire)" stroke-width="4" stroke-opacity="0.75"/>
    <line x1="130" y1="140" x2="165" y2="168" stroke="var(--node-ring)" stroke-width="4"/>
    <circle cx="196" cy="196" r="40" fill="#ffffff" stroke="var(--node-ring)" stroke-width="6"/>
    <circle cx="196" cy="196" r="6" fill="var(--wire)"/>
    <line x1="1040" y1="92" x2="1093" y2="92" stroke="var(--node-ring)" stroke-width="4"/>
    <circle cx="1135" cy="92" r="40" fill="#ffffff" stroke="var(--node-ring)" stroke-width="6"/>
    <circle cx="1135" cy="92" r="6" fill="var(--wire)"/>
  </svg>

  <svg class="corner-banner" viewBox="0 0 260 300" aria-hidden="true">
    <defs>
      <linearGradient id="cornerFill" x1="0" y1="0" x2="1" y2="1">
        <stop offset="0" stop-color="var(--corner-dark)"/>
        <stop offset="1" stop-color="var(--corner-light)"/>
      </linearGradient>
    </defs>
    <polygon points="0,0 240,0 0,285" fill="url(#cornerFill)"/>
  </svg>
  <div class="corner-text">I AM<br>CONNECTED<br>TO</div>

  <div class="brand">
    <span class="brand-dot"></span>
    <span class="brand-name">DOVERN</span>
  </div>

  <p class="contact">Contact us at :<span class="phone">555 814 2063</span></p>

  <h1 class="headline">
    The fastest high&nbsp; speed<br>
    internet available.<br>
    <span class="fiber">FIBER OPTIC</span><br>
    <span class="fast">FAST</span>
  </h1>

  <p class="more">Find out more at :<span class="url">WWW.DOVERNETLINK.EXAMPLE</span></p>
</div>
</body>
</html>
```